Brisk Nova residential and commercial cleaning

We need a Business card design for a new residential and commercial cleaning company based in UAE- Abu Dhabi named (BRISK NOVA)
we provide a residential cleaning service based in hourly rate (Maid Rent - Baby Setting), Also a commercial and offices cleaning.
Our logo is attached for your reference

Target Market(s)

Women who are 22 to 60 years old.

Industry/Entity Type

Residential

Requirements
Should not have
• it should not have an old-style fonts

```html
<!DOCTYPE html>
<html lang="en">
<head>
<meta charset="utf-8">
<title>Brisk Nova – Business Card</title>
<link rel="stylesheet" href="https://fonts.googleapis.com/css2?family=Open+Sans:wght@400;600;700&display=swap">
<style>
  :root {
    --page-bg: #e9e6e1;
    --card-white: #ffffff;
    --brand-blue: #1a6fb5;
    --brand-blue-deep: #0f5a9c;
    --brand-green: #8cc63f;
    --text-white: #ffffff;
    --text-grey: #555b61;
    --faint-blue: #dce9f4;
    --faint-green: #e6f2d6;
  }
  html, body {
    margin: 0;
    padding: 0;
    width: 1200px;
    height: 900px;
    overflow: hidden;
    background: var(--page-bg);
    font-family: "Open Sans", sans-serif;
  }
  .canvas {
    position: relative;
    width: 1200px;
    height: 900px;
  }
  .card {
    position: absolute;
    left: 320px;
    width: 560px;
    height: 320px;
    border-radius: 18px;
    background: var(--card-white);
    box-shadow: 0 10px 26px rgba(0,0,0,0.18);
    overflow: hidden;
  }
  .card--back { top: 90px; }
  .card--front { top: 480px; }

  /* Back side */
  .back-decoration {
    position: absolute;
    left: 20px;
    top: -30px;
    width: 300px;
    height: 300px;
    border-radius: 50%;
    background: radial-gradient(circle at 45% 45%, var(--faint-blue) 0%, var(--faint-green) 55%, rgba(255,255,255,0) 72%);
  }
  .back-brand {
    position: absolute;
    right: 40px;
    bottom: 58px;
    font-size: 42px;
    font-weight: 700;
    color: var(--brand-blue);
    letter-spacing: -0.5px;
    margin: 0;
  }
  .back-web {
    position: absolute;
    right: 44px;
    bottom: 30px;
    font-size: 13px;
    color: var(--text-grey);
    letter-spacing: 3px;
    margin: 0;
  }

  /* Front side */
  .front-shapes {
    position: absolute;
    inset: 0;
  }
  .contact-block {
    position: absolute;
    left: 38px;
    top: 30px;
    color: var(--text-white);
  }
  .contact-name {
    margin: 0;
    font-size: 21px;
    font-weight: 700;
  }
  .contact-role {
    margin: 0 0 16px;
    font-size: 13px;
  }
  .contact-address {
    margin: 0 0 12px;
    font-size: 13px;
    line-height: 1.35;
  }
  .contact-list {
    list-style: none;
    margin: 0;
    padding: 0;
    font-size: 13px;
  }
  .contact-list li {
    display: flex;
    align-items: center;
    gap: 8px;
    height: 21px;
  }
  .contact-list svg {
    width: 13px;
    height: 13px;
    flex: none;
  }
  .front-brand {
    position: absolute;
    left: 318px;
    top: 150px;
    display: flex;
    align-items: center;
    gap: 14px;
  }
  .front-brand-name {
    margin: 0;
    font-size: 34px;
    font-weight: 700;
    color: var(--brand-blue);
    letter-spacing: -0.5px;
  }
  .front-brand-mark {
    width: 52px;
    height: 52px;
    border-radius: 50%;
    border: 3px solid var(--brand-green);
    box-sizing: border-box;
  }
</style>
</head>
<body>
<main class="canvas">

  <section class="card card--back" aria-label="Card back">
    <div class="back-decoration" role="img" aria-label="Faint brand decoration in soft blue and green"></div>
    <p class="back-brand">Brisk Nova</p>
    <p class="back-web">www.brisknova.ae</p>
  </section>

  <section class="card card--front" aria-label="Card front">
    <svg class="front-shapes" width="560" height="320" viewBox="0 0 560 320" aria-hidden="true">
      <defs>
        <linearGradient id="blueFill" x1="0" y1="0" x2="1" y2="1">
          <stop offset="0" stop-color="var(--brand-blue-deep)"/>
          <stop offset="1" stop-color="var(--brand-blue)"/>
        </linearGradient>
        <mask id="blueMask">
          <rect width="560" height="320" fill="#fff"/>
          <circle cx="600" cy="330" r="335" fill="#000"/>
        </mask>
      </defs>
      <rect width="560" height="320" fill="url(#blueFill)" mask="url(#blueMask)"/>
      <circle cx="600" cy="330" r="322" fill="none" stroke="var(--brand-green)" stroke-width="5"/>
    </svg>

    <div class="contact-block">
      <p class="contact-name">Layla Haddad</p>
      <p class="contact-role">Director</p>
      <p class="contact-address">Office 14, Corniche Road<br>Abu Dhabi, UAE</p>
      <ul class="contact-list">
        <li>
          <svg viewBox="0 0 16 16"><path d="M2 5c0-2 2-3 6-3s6 1 6 3l-3 1-1-2H6L5 6zM4 7h8l2 7H2z" fill="#fff"/></svg>
          02 555 0142
        </li>
        <li>
          <svg viewBox="0 0 16 16"><rect x="4" y="1" width="8" height="14" rx="1.5" fill="none" stroke="#fff" stroke-width="1.6"/><circle cx="8" cy="12.5" r="0.9" fill="#fff"/></svg>
          050 555 0187
        </li>
        <li>
          <svg viewBox="0 0 16 16"><rect x="1" y="6" width="14" height="8" rx="1" fill="#fff"/><rect x="4" y="2" width="8" height="5" fill="none" stroke="#fff" stroke-width="1.4"/></svg>
          02 555 0143
        </li>
        <li>
          <svg viewBox="0 0 16 16"><rect x="1" y="3" width="14" height="10" rx="1" fill="#fff"/><path d="M1.5 3.5 8 9l6.5-5.5" fill="none" stroke="var(--brand-blue)" stroke-width="1.3"/></svg>
          hello@brisknova.ae
        </li>
        <li>
          <svg viewBox="0 0 16 16"><circle cx="8" cy="8" r="6.5" fill="none" stroke="#fff" stroke-width="1.4"/><ellipse cx="8" cy="8" rx="2.8" ry="6.5" fill="none" stroke="#fff" stroke-width="1.2"/><path d="M1.5 8h13" stroke="#fff" stroke-width="1.2"/></svg>
          www.brisknova.ae
        </li>
      </ul>
    </div>

    <div class="front-brand">
      <p class="front-brand-name">Brisk Nova</p>
      <span class="front-brand-mark"></span>
    </div>
  </section>

</main>
</body>
</html>
```